Holvern Incorporated

Holvern is a business that provides consulting, and manages and supplies trades persons in the construction and heavy industries sector. We build, do maintenance, install machinery, and can manage projects or jobs. Would like or prefer more clean, classic designs. Blacks/greys, but open to almost anything.

Target Market(s)

Industrial/Construction/Manufacturing

Industry/Entity Type

Construction Company

Contact Information for Business Card

Clean, business name on the front, possibly have the details on the back, but open to any ideas.

Logo Text

We currently do not have a slogan, open to ideas

Font styles to use
Serif
Sans Serif

Colors

Designer to choose colors to be used in the design.

Requirements
Should not have
• the oval is not my logo, was just an idea. please don't send 20 designs with the oval

```html
<!DOCTYPE html>
<html lang="en">
<head>
<meta charset="utf-8">
<title>Holvern Incorporated – Business Card</title>
<link rel="stylesheet" href="https://fonts.googleapis.com/css2?family=Arimo:wght@400&family=Tinos:wght@700&display=swap">
<style>
  :root {
    --card-black: #000000;
    --page-white: #ffffff;
    --curl-light: #dadada;
    --curl-mid: #bdbdbd;
    --text-white: #ffffff;
    --text-grey: #c4c4c4;
    --brand-grey: #d9d9d9;
  }
  html, body {
    margin: 0;
    padding: 0;
    overflow: hidden;
    background: var(--page-white);
  }
  .card {
    position: relative;
    width: 1200px;
    height: 684px;
    overflow: hidden;
    background: var(--page-white);
  }
  .card-shape {
    position: absolute;
    inset: 0;
    width: 1200px;
    height: 684px;
  }
  .shape-light { fill: var(--curl-light); }
  .shape-mid { fill: var(--curl-mid); }
  .shape-black { fill: var(--card-black); }

  .person {
    position: absolute;
    left: 103px;
    top: 218px;
    width: 395px;
    text-align: right;
  }
  .person-name {
    margin: 0;
    font-family: "Tinos", "Times New Roman", serif;
    font-weight: 700;
    font-size: 42px;
    line-height: 48px;
    color: var(--text-white);
    letter-spacing: 0.5px;
  }
  .person-rule {
    height: 2px;
    background: var(--text-white);
    margin: 0;
  }
  .person-role {
    margin: 3px 0 0;
    font-family: "Arimo", Arial, sans-serif;
    font-size: 21px;
    color: var(--text-grey);
  }

  .brand {
    position: absolute;
    left: 652px;
    top: 282px;
    margin: 0;
    font-family: "Tinos", "Times New Roman", serif;
    font-weight: 700;
    font-size: 84px;
    line-height: 96px;
    color: var(--brand-grey);
    letter-spacing: 1px;
  }

  .contacts {
    position: absolute;
    left: 103px;
    top: 431px;
    margin: 0;
    padding: 0;
    list-style: none;
  }
  .contact-item {
    display: flex;
    align-items: center;
    height: 39.5px;
    font-family: "Arimo", Arial, sans-serif;
    font-size: 22px;
    color: var(--text-white);
  }
  .contact-icon {
    width: 32px;
    height: 32px;
    margin-right: 13px;
    flex: none;
  }
  .contact-icon .ink { fill: var(--text-white); }
  .contact-icon .stroke { fill: none; stroke: var(--text-white); stroke-width: 2; }
</style>
</head>
<body>
<div class="card">
  <svg class="card-shape" viewBox="0 0 1075 613" preserveAspectRatio="none" aria-hidden="true">
    <path class="shape-light" d="M0,0 H1055 C1058,250 1058,420 1053,540 C1050,590 1025,608 990,610 L700,613 H0 Z"/>
    <path class="shape-mid" d="M0,0 H1055 C1060,260 1045,430 975,515 C905,590 800,606 715,612 H0 Z"/>
    <path class="shape-black" d="M0,0 H1055 C1050,250 1025,420 945,505 C870,580 780,602 700,610 H0 Z"/>
  </svg>

  <div class="person">
    <h1 class="person-name">RANE COLBY</h1>
    <div class="person-rule"></div>
    <p class="person-role">Lorem Ipsum</p>
  </div>

  <p class="brand">Holvern</p>

  <ul class="contacts">
    <li class="contact-item">
      <svg class="contact-icon" viewBox="0 0 24 24" aria-hidden="true">
        <path class="ink" d="M6.6 10.8a15.2 15.2 0 0 0 6.6 6.6l2.2-2.2a1 1 0 0 1 1-.25 11.4 11.4 0 0 0 3.6.57 1 1 0 0 1 1 1V20a1 1 0 0 1-1 1A17 17 0 0 1 3 4a1 1 0 0 1 1-1h3.5a1 1 0 0 1 1 1c0 1.25.2 2.45.57 3.57a1 1 0 0 1-.25 1z"/>
      </svg>
      <span>(+92-34-5550172</span>
    </li>
    <li class="contact-item">
      <svg class="contact-icon" viewBox="0 0 24 24" aria-hidden="true">
        <rect class="ink" x="2" y="5" width="20" height="14"/>
        <path d="M2.5 5.5 12 13l9.5-7.5M2.5 18.5l7-6.5M21.5 18.5l-7-6.5" fill="none" stroke="#000" stroke-width="1.3"/>
      </svg>
      <span>simply dummy text@mailbox.com</span>
    </li>
    <li class="contact-item">
      <svg class="contact-icon" viewBox="0 0 24 24" aria-hidden="true">
        <circle class="stroke" cx="12" cy="12" r="10"/>
        <ellipse class="stroke" cx="12" cy="12" rx="4.5" ry="10"/>
        <path class="stroke" d="M2 12h20M3.5 7h17M3.5 17h17"/>
      </svg>
      <span>simply dummy text.com</span>
    </li>
    <li class="contact-item">
      <svg class="contact-icon" viewBox="0 0 24 24" aria-hidden="true">
        <path class="ink" d="M12 2a7 7 0 0 0-7 7c0 5.2 7 13 7 13s7-7.8 7-13a7 7 0 0 0-7-7zm0 9.5A2.5 2.5 0 1 1 12 6.5a2.5 2.5 0 0 1 0 5z"/>
      </svg>
      <span>simply dummy text</span>
    </li>
  </ul>
</div>
</body>
</html>
```